7K packaging design

We are a wholesaler for Automotive Spare Parts in Jordan and Iraq market and we needs to import spare parts from China under our company private brand "7K"
The 7K brand’s product lines include Filtration, Braking Systems, Wheels, Wheel Bolts & Nuts, Shock Absorbers, Sensors, Cooling Systems, Axles and more.
The aim of the project is to unify the brand packaging across all the product lines , we will start by the brake pads then based on the approved design we will do the other products

Target Market(s)

Jordan , Iraq Market

Industry/Entity Type

Automotive spare parts

Requirements
Must have
• Name of the product :Ceramic brake pads specs : Superior stopping power Noise suppression Low Dust Technology Made in china
Nice to have
• Brake pad outline image on the box
Should not have
• Blue color

```html
<!DOCTYPE html>
<html lang="en">
<head>
<meta charset="utf-8">
<title>7K packaging design – Ceramic Brake Pads box dieline</title>
<link href="https://fonts.googleapis.com/css2?family=Audiowide&family=Roboto:wght@500&display=swap" rel="stylesheet">
<style>
  :root{
    --red:#ff0010;
    --red-deep:#b00010;
    --red-dark:#4a0006;
    --charcoal:#333333;
    --steel:#8a8a8a;
    --steel-dark:#5e5e5e;
    --silver:#d8d8d8;
    --white:#ffffff;
    --cut:#3aa9bd;
    --paper:#ffffff;
  }
  *{box-sizing:border-box;margin:0;padding:0}
  html,body{width:1200px;height:660px;overflow:hidden;background:var(--paper)}
  .sheet{position:relative;width:1200px;height:660px}
  .dieline{position:absolute;top:34px;width:537px;height:600px}
  .dieline--truck{left:33px}
  .dieline--car{left:637px}

  .part{position:absolute;border:0.6px solid var(--cut)}
  .part--dark{background:var(--charcoal)}
  .lid{top:0;left:130px;width:276px;height:111px;
    background:linear-gradient(180deg,var(--red-dark) 0%,var(--red-deep) 45%,var(--red) 100%)}
  .lid-side{top:0;width:130px;height:111px}
  .lid-side--l{left:0}.lid-side--r{left:406px;width:131px}
  .back{top:111px;left:130px;width:276px;height:132px;
    background:linear-gradient(180deg,var(--red-dark) 0%,var(--red-deep) 35%,var(--red) 85%)}
  .flap{top:131px;width:130px;height:112px}
  .flap--l{left:0}.flap--r{left:406px;width:131px}
  .flap-tab{position:absolute;bottom:0;left:42px;width:47px;height:8px;border:0.6px solid var(--cut);border-bottom:none}

  .side-photo{top:243px;width:130px;height:111px;overflow:hidden}
  .side-photo--l{left:0}
  .side-photo--r{left:406px;width:131px}
  .photo{background:linear-gradient(160deg,#b9b9b9 0%,#7d7d7d 45%,#4d4d4d 100%)}
  .dieline--car .photo{background:linear-gradient(160deg,#cfcfcf 0%,#8d8d8d 50%,#5a5a5a 100%)}

  .side-red{top:354px;width:130px;height:107px;
    background:linear-gradient(200deg,var(--red) 0%,var(--red) 45%,var(--red-deep) 80%,var(--red-dark) 100%)}
  .side-red--l{left:0}.side-red--r{left:406px;width:131px}
  .side-tab{position:absolute;top:461px;width:52px;height:5px;border:0.6px solid var(--cut);border-top:none}
  .side-tab--l{left:40px}.side-tab--r{left:446px}

  .front{top:354px;left:130px;width:276px;height:130px;overflow:hidden;
    background:linear-gradient(190deg,var(--red-deep) 0%,var(--red) 35%,var(--red) 65%,var(--red-deep) 100%)}
  .base-flap{position:absolute;top:484px;width:106px;height:112px}

  .brand{display:flex;align-items:center;gap:4px;font-family:'Audiowide',sans-serif;color:var(--white);line-height:1}
  .brand-dot{width:10px;height:10px;border-radius:50%;background:var(--white)}
  .title{font-family:'Audiowide',sans-serif;color:var(--white);line-height:0.95}
  .pad-art{position:absolute;border-radius:10px;
    background:linear-gradient(160deg,rgba(255,255,255,.14),rgba(255,255,255,.04))}

  .features{display:flex;align-items:center;gap:8px;font-family:'Roboto',sans-serif;font-weight:500;color:var(--white)}
  .feature{display:flex;align-items:center;gap:3px;font-size:3.6px;line-height:1.05;letter-spacing:.1px}
  .feature svg{width:11px;height:11px;flex:none}

  /* front main face */
  .front .brand{position:absolute;left:12px;top:12px;font-size:22px}
  .front .brand .brand-dot{width:12px;height:12px}
  .front .title{position:absolute;left:13px;top:70px;font-size:9.6px;font-style:normal}
  .front .pad-art{left:128px;top:18px;width:138px;height:88px}
  .front .features{position:absolute;left:12px;top:101px}

  /* cover face: used on base and (turned) on top of front */
  .cover{left:130px;width:276px;height:111px;overflow:hidden;
    background:linear-gradient(180deg,var(--red-dark) 0%,var(--red-deep) 60%,var(--red) 100%)}
  .cover--base{top:484px;height:112px}
  .cover--top{top:243px;transform:rotate(180deg)}
  .cover-stripe{position:absolute;inset:0;background:var(--silver);clip-path:polygon(0 0,57% 0,40% 100%,0 100%)}
  .cover-photo{position:absolute;inset:0;clip-path:polygon(0 0,54.5% 0,37.5% 100%,0 100%)}
  .cover .pad-art{left:145px;top:8px;width:122px;height:80px}
  .cover .brand{position:absolute;left:9px;top:10px;font-size:16px}
  .cover .title{position:absolute;left:9px;top:65px;font-size:11px;text-shadow:none}
  .cover-strip{position:absolute;right:0;bottom:0;height:21px;width:180px;
    background:linear-gradient(90deg,var(--steel-dark),var(--steel));clip-path:polygon(6% 0,100% 0,100% 100%,0 100%)}
  .cover .features{position:absolute;right:8px;bottom:5px}

  /* right side panel (reads upside down on the flat) */
  .side-label{position:absolute;inset:0;transform:rotate(180deg)}
  .side-label .brand{position:absolute;right:22px;top:20px;font-size:20px}
  .side-label .title{position:absolute;left:12px;bottom:20px;font-size:7.6px;white-space:nowrap}
  .side-label .origin{position:absolute;left:0;right:0;bottom:7px;text-align:center;
    font-family:'Roboto',sans-serif;font-weight:500;font-size:4.6px;color:var(--white);letter-spacing:.2px}
</style>
</head>
<body>
<main class="sheet">

  <!-- dieline A : truck variant -->
  <section class="dieline dieline--truck" aria-label="Brake pad box dieline, truck edition">
    <div class="part part--dark lid-side lid-side--l"></div>
    <div class="part lid"></div>
    <div class="part part--dark lid-side lid-side--r"></div>

    <div class="part part--dark flap flap--l"><span class="flap-tab"></span></div>
    <div class="part back"></div>
    <div class="part part--dark flap flap--r"><span class="flap-tab"></span></div>

    <div class="part side-photo side-photo--l photo" role="img" aria-label="Photo of a truck front in grey tones"></div>
    <div class="part cover cover--top">
      <div class="pad-art" role="img" aria-label="White line drawing of a pair of brake pads"></div>
      <div class="cover-stripe"></div>
      <div class="cover-photo photo" role="img" aria-label="Photo of a truck in grey tones"></div>
      <div class="brand">7K<span class="brand-dot"></span></div>
      <div class="title">Ceramic<br>Brake<br>Pads</div>
      <div class="cover-strip"></div>
      <div class="features">
        <div class="feature"><svg viewBox="0 0 12 12"><circle cx="6" cy="6" r="5.2" fill="none" stroke="#fff" stroke-width="1"/><circle cx="6" cy="6" r="2.2" fill="none" stroke="#fff" stroke-width="1"/></svg><span>SUPERIOR<br>STOPPING<br>POWER</span></div>
        <div class="feature"><svg viewBox="0 0 12 12"><path d="M1 4.5h2.5L6.5 2v8L3.5 7.5H1z" fill="none" stroke="#fff" stroke-width="0.9"/><path d="M8 3.5l3-1.5M8 6h3.5M8 8.5l3 1.5" stroke="#fff" stroke-width="0.9"/></svg><span>NOISE<br>SUPPRESSION</span></div>
        <div class="feature"><svg viewBox="0 0 12 12"><circle cx="6" cy="6" r="5" fill="none" stroke="#fff" stroke-width="0.9" stroke-dasharray="1.4 1"/><circle cx="5" cy="5" r="0.8" fill="#fff"/><circle cx="7.4" cy="6.6" r="0.8" fill="#fff"/></svg><span>LOW DUST<br>TECHNOLOGY</span></div>
      </div>
    </div>
    <div class="part side-photo side-photo--r photo" role="img" aria-label="Photo of a truck front in grey tones">
      <div class="side-label">
        <div class="brand">7K<span class="brand-dot"></span></div>
        <div class="title">Ceramic Brake Pads</div>
        <div class="origin">MADE IN CHINA</div>
      </div>
    </div>

    <div class="part side-red side-red--l"></div>
    <div class="part front">
      <div class="brand">7K<span class="brand-dot"></span></div>
      <div class="pad-art" role="img" aria-label="White line drawing of a pair of brake pads"></div>
      <div class="title">Ceramic Brake Pads</div>
      <div class="features">
        <div class="feature"><svg viewBox="0 0 12 12"><circle cx="6" cy="6" r="5.2" fill="none" stroke="#fff" stroke-width="1"/><circle cx="6" cy="6" r="2.2" fill="none" stroke="#fff" stroke-width="1"/></svg><span>SUPERIOR<br>STOPPING<br>POWER</span></div>
        <div class="feature"><svg viewBox="0 0 12 12"><path d="M1 4.5h2.5L6.5 2v8L3.5 7.5H1z" fill="none" stroke="#fff" stroke-width="0.9"/><path d="M8 3.5l3-1.5M8 6h3.5M8 8.5l3 1.5" stroke="#fff" stroke-width="0.9"/></svg><span>NOISE<br>SUPPRESSION</span></div>
        <div class="feature"><svg viewBox="0 0 12 12"><circle cx="6" cy="6" r="5" fill="none" stroke="#fff" stroke-width="0.9" stroke-dasharray="1.4 1"/><circle cx="5" cy="5" r="0.8" fill="#fff"/><circle cx="7.4" cy="6.6" r="0.8" fill="#fff"/></svg><span>LOW DUST<br>TECHNOLOGY</span></div>
      </div>
    </div>
    <div class="part side-red side-red--r"></div>
    <span class="side-tab side-tab--l"></span><span class="side-tab side-tab--r"></span>

    <svg class="base-flap" style="left:31px" viewBox="0 0 106 112">
      <defs><linearGradient id="flapA" x1="0" y1="0" x2="0.4" y2="1"><stop offset="0" stop-color="var(--red)"/><stop offset="0.55" stop-color="var(--red)"/><stop offset="1" stop-color="var(--red-deep)"/></linearGradient></defs>
      <path d="M99 0H14C4 0 0 6 0 16c0 40 28 80 62 94l37 1z" fill="url(#flapA)" stroke="var(--cut)" stroke-width="0.6"/>
    </svg>
    <div class="part cover cover--base">
      <div class="pad-art" role="img" aria-label="White line drawing of a pair of brake pads"></div>
      <div class="cover-stripe"></div>
      <div class="cover-photo photo" role="img" aria-label="Photo of a truck in grey tones"></div>
      <div class="brand">7K<span class="brand-dot"></span></div>
      <div class="title">Ceramic<br>Brake<br>Pads</div>
      <div class="cover-strip"></div>
      <div class="features">
        <div class="feature"><svg viewBox="0 0 12 12"><circle cx="6" cy="6" r="5.2" fill="none" stroke="#fff" stroke-width="1"/><circle cx="6" cy="6" r="2.2" fill="none" stroke="#fff" stroke-width="1"/></svg><span>SUPERIOR<br>STOPPING<br>POWER</span></div>
        <div class="feature"><svg viewBox="0 0 12 12"><path d="M1 4.5h2.5L6.5 2v8L3.5 7.5H1z" fill="none" stroke="#fff" stroke-width="0.9"/><path d="M8 3.5l3-1.5M8 6h3.5M8 8.5l3 1.5" stroke="#fff" stroke-width="0.9"/></svg><span>NOISE<br>SUPPRESSION</span></div>
        <div class="feature"><svg viewBox="0 0 12 12"><circle cx="6" cy="6" r="5" fill="none" stroke="#fff" stroke-width="0.9" stroke-dasharray="1.4 1"/><circle cx="5" cy="5" r="0.8" fill="#fff"/><circle cx="7.4" cy="6.6" r="0.8" fill="#fff"/></svg><span>LOW DUST<br>TECHNOLOGY</span></div>
      </div>
    </div>
    <svg class="base-flap" style="left:406px" viewBox="0 0 106 112">
      <path d="M7 0h85c10 0 14 6 14 16 0 40-28 80-62 94L7 111z" fill="url(#flapA)" stroke="var(--cut)" stroke-width="0.6"/>
    </svg>
  </section>

  <!-- dieline B : car variant -->
  <section class="dieline dieline--car" aria-label="Brake pad box dieline, car edition">
    <div class="part part--dark lid-side lid-side--l"></div>
    <div class="part lid"></div>
    <div class="part part--dark lid-side lid-side--r"></div>

    <div class="part part--dark flap flap--l"><span class="flap-tab"></span></div>
    <div class="part back"></div>
    <div class="part part--dark flap flap--r"><span class="flap-tab"></span></div>

    <div class="part side-photo side-photo--l photo" role="img" aria-label="Photo of a sports car in grey tones"></div>
    <div class="part cover cover--top">
      <div class="pad-art" role="img" aria-label="White line drawing of a pair of brake pads"></div>
      <div class="cover-stripe"></div>
      <div class="cover-photo photo" role="img" aria-label="Photo of a sports car in grey tones"></div>
      <div class="brand">7K<span class="brand-dot"></span></div>
      <div class="title">Ceramic<br>Brake<br>Pads</div>
      <div class="cover-strip"></div>
      <div class="features">
        <div class="feature"><svg viewBox="0 0 12 12"><circle cx="6" cy="6" r="5.2" fill="none" stroke="#fff" stroke-width="1"/><circle cx="6" cy="6" r="2.2" fill="none" stroke="#fff" stroke-width="1"/></svg><span>SUPERIOR<br>STOPPING<br>POWER</span></div>
        <div class="feature"><svg viewBox="0 0 12 12"><path d="M1 4.5h2.5L6.5 2v8L3.5 7.5H1z" fill="none" stroke="#fff" stroke-width="0.9"/><path d="M8 3.5l3-1.5M8 6h3.5M8 8.5l3 1.5" stroke="#fff" stroke-width="0.9"/></svg><span>NOISE<br>SUPPRESSION</span></div>
        <div class="feature"><svg viewBox="0 0 12 12"><circle cx="6" cy="6" r="5" fill="none" stroke="#fff" stroke-width="0.9" stroke-dasharray="1.4 1"/><circle cx="5" cy="5" r="0.8" fill="#fff"/><circle cx="7.4" cy="6.6" r="0.8" fill="#fff"/></svg><span>LOW DUST<br>TECHNOLOGY</span></div>
      </div>
    </div>
    <div class="part side-photo side-photo--r photo" role="img" aria-label="Photo of a sports car in grey tones">
      <div class="side-label">
        <div class="brand">7K<span class="brand-dot"></span></div>
        <div class="title">Ceramic Brake Pads</div>
        <div class="origin">MADE IN CHINA</div>
      </div>
    </div>

    <div class="part side-red side-red--l"></div>
    <div class="part front">
      <div class="brand">7K<span class="brand-dot"></span></div>
      <div class="pad-art" role="img" aria-label="White line drawing of a pair of brake pads"></div>
      <div class="title">Ceramic Brake Pads</div>
      <div class="features">
        <div class="feature"><svg viewBox="0 0 12 12"><circle cx="6" cy="6" r="5.2" fill="none" stroke="#fff" stroke-width="1"/><circle cx="6" cy="6" r="2.2" fill="none" stroke="#fff" stroke-width="1"/></svg><span>SUPERIOR<br>STOPPING<br>POWER</span></div>
        <div class="feature"><svg viewBox="0 0 12 12"><path d="M1 4.5h2.5L6.5 2v8L3.5 7.5H1z" fill="none" stroke="#fff" stroke-width="0.9"/><path d="M8 3.5l3-1.5M8 6h3.5M8 8.5l3 1.5" stroke="#fff" stroke-width="0.9"/></svg><span>NOISE<br>SUPPRESSION</span></div>
        <div class="feature"><svg viewBox="0 0 12 12"><circle cx="6" cy="6" r="5" fill="none" stroke="#fff" stroke-width="0.9" stroke-dasharray="1.4 1"/><circle cx="5" cy="5" r="0.8" fill="#fff"/><circle cx="7.4" cy="6.6" r="0.8" fill="#fff"/></svg><span>LOW DUST<br>TECHNOLOGY</span></div>
      </div>
    </div>
    <div class="part side-red side-red--r"></div>
    <span class="side-tab side-tab--l"></span><span class="side-tab side-tab--r"></span>

    <svg class="base-flap" style="left:31px" viewBox="0 0 106 112">
      <path d="M99 0H14C4 0 0 6 0 16c0 40 28 80 62 94l37 1z" fill="url(#flapA)" stroke="var(--cut)" stroke-width="0.6"/>
    </svg>
    <div class="part cover cover--base">
      <div class="pad-art" role="img" aria-label="White line drawing of a pair of brake pads"></div>
      <div class="cover-stripe"></div>
      <div class="cover-photo photo" role="img" aria-label="Photo of a sports car in grey tones"></div>
      <div class="brand">7K<span class="brand-dot"></span></div>
      <div class="title">Ceramic<br>Brake<br>Pads</div>
      <div class="cover-strip"></div>
      <div class="features">
        <div class="feature"><svg viewBox="0 0 12 12"><circle cx="6" cy="6" r="5.2" fill="none" stroke="#fff" stroke-width="1"/><circle cx="6" cy="6" r="2.2" fill="none" stroke="#fff" stroke-width="1"/></svg><span>SUPERIOR<br>STOPPING<br>POWER</span></div>
        <div class="feature"><svg viewBox="0 0 12 12"><path d="M1 4.5h2.5L6.5 2v8L3.5 7.5H1z" fill="none" stroke="#fff" stroke-width="0.9"/><path d="M8 3.5l3-1.5M8 6h3.5M8 8.5l3 1.5" stroke="#fff" stroke-width="0.9"/></svg><span>NOISE<br>SUPPRESSION</span></div>
        <div class="feature"><svg viewBox="0 0 12 12"><circle cx="6" cy="6" r="5" fill="none" stroke="#fff" stroke-width="0.9" stroke-dasharray="1.4 1"/><circle cx="5" cy="5" r="0.8" fill="#fff"/><circle cx="7.4" cy="6.6" r="0.8" fill="#fff"/></svg><span>LOW DUST<br>TECHNOLOGY</span></div>
      </div>
    </div>
    <svg class="base-flap" style="left:406px" viewBox="0 0 106 112">
      <path d="M7 0h85c10 0 14 6 14 16 0 40-28 80-62 94L7 111z" fill="url(#flapA)" stroke="var(--cut)" stroke-width="0.6"/>
    </svg>
  </section>

</main>
</body>
</html>
```